Updated Business Card Design more modern and eye catching

looking for something more dynamic than the sterile card we have now. Please take a look at our web site www.quarvinstores.net to see what we do. only looking for the front side of the card for now. I've also attached a sample of a card with raised spot uv ink - it might be cool to incorporate something like that. Card should be bold yet serious. No frilly or scrolly stuff on it.
Updates
Target Market(s)
We do decor and signage for retail business and supermarkets. Our new name should reflect that we're hip but serious.
Contact Information for Business Card
standard business card size - horizontal preferred
Font styles to use
Requirements
Must have
- Current logo and colors cannot be changed.
Nice to have
- Must have information shown on existing card but open to some changes. Okay to consider spot uv.
Should not have
- Not busy with pictures in the background.

```html
<!DOCTYPE html>
<html lang="en">
<head>
<meta charset="utf-8">
<title>Quarvin Stores – Business Card</title>
<link rel="stylesheet" href="https://fonts.googleapis.com/css2?family=Exo+2:wght@400;600;700&display=swap">
<style>
  :root {
    --bg: #d9d9d9;
    --ink: #0b0b0b;
    --paper: #ffffff;
    --gold: #b3a955;
    --text: #141414;
  }
  * { margin: 0; padding: 0; box-sizing: border-box; }
  html, body { width: 1200px; height: 884px; overflow: hidden; }
  body {
    background: var(--bg);
    font-family: "Exo 2", sans-serif;
    color: var(--text);
    position: relative;
  }
  .card {
    position: absolute;
    left: 75px; top: 142px;
    width: 1050px; height: 600px;
    background: var(--paper);
    overflow: hidden;
  }
  .card__header {
    position: absolute;
    left: 0; top: 0; right: 0;
    height: 172px;
    background: var(--ink);
    display: flex;
    align-items: center;
    justify-content: center;
    gap: 26px;
  }
  .brand__mark {
    width: 44px; height: 44px;
    border: 3px solid var(--gold);
  }
  .brand__name {
    font-weight: 600;
    font-size: 62px;
    letter-spacing: 10px;
    color: var(--gold);
    text-transform: uppercase;
  }
  .card__stripe {
    position: absolute;
    left: 0; top: 172px; bottom: 0;
    width: 36px;
    background: var(--gold);
  }
  .person {
    position: absolute;
    left: 82px; top: 212px;
  }
  .person__name {
    font-weight: 700;
    font-size: 38px;
    color: var(--gold);
    text-transform: uppercase;
    line-height: 1;
  }
  .person__title {
    font-size: 25px;
    font-style: italic;
    margin-top: 8px;
  }
  .rule {
    position: absolute;
    left: 76px; right: 76px;
    height: 2px;
    background: var(--gold);
  }
  .rule--top { top: 318px; }
  .rule--bottom { top: 470px; }
  .contact {
    position: absolute;
    font-size: 26px;
    line-height: 1.55;
  }
  .contact--phones { left: 82px; top: 338px; }
  .contact--online { right: 82px; top: 392px; }
  .contact__row { display: flex; align-items: center; gap: 12px; }
  .contact__row svg { width: 22px; height: 22px; flex: none; }
  .address {
    position: absolute;
    left: 82px; top: 498px;
    font-size: 27px;
  }
</style>
</head>
<body>
  <main class="card">
    <header class="card__header">
      <span class="brand__mark"></span>
      <span class="brand__name">Quarvin Stores</span>
    </header>
    <div class="card__stripe"></div>

    <section class="person">
      <h1 class="person__name">Mara Dellano</h1>
      <p class="person__title">Vice-President</p>
    </section>

    <div class="rule rule--top"></div>

    <section class="contact contact--phones">
      <p class="contact__row">
        <svg viewBox="0 0 24 24" fill="none" stroke="#b3a955" stroke-width="2"><rect x="6" y="2" width="12" height="20" rx="2"/><line x1="11" y1="18" x2="13" y2="18"/></svg>
        555.218.4407
      </p>
      <p class="contact__row">
        <svg viewBox="0 0 24 24" fill="#b3a955"><path d="M6.6 10.8a15 15 0 0 0 6.6 6.6l2.2-2.2a1 1 0 0 1 1-.25 11.4 11.4 0 0 0 3.6.57 1 1 0 0 1 1 1V20a1 1 0 0 1-1 1A17 17 0 0 1 3 4a1 1 0 0 1 1-1h3.5a1 1 0 0 1 1 1c0 1.25.2 2.45.57 3.57a1 1 0 0 1-.25 1z"/></svg>
        555.630.1182 ext. 3
      </p>
    </section>

    <section class="contact contact--online">
      <p class="contact__row">
        <svg viewBox="0 0 24 24" fill="none" stroke="#b3a955" stroke-width="2"><rect x="2" y="5" width="20" height="14"/><polyline points="2,5 12,13 22,5"/></svg>
        Mara@QuarvinStores.net
      </p>
      <p class="contact__row">
        <svg viewBox="0 0 24 24" fill="none" stroke="#b3a955" stroke-width="1.8"><circle cx="12" cy="12" r="10"/><ellipse cx="12" cy="12" rx="4.5" ry="10"/><line x1="2" y1="12" x2="22" y2="12"/></svg>
        www.QuarvinStores.net
      </p>
    </section>

    <div class="rule rule--bottom"></div>

    <p class="address">4410 Commerce Way, Lake Harlow, FL 30187</p>
  </main>
</body>
</html>
```